Web Design for Harbor Ledger Associates

Harbor Ledger Associates needs the photoshop files for a simple, clean and professional website design. The company is building a network of bookkeepers/accountants to handle outsourced bookkeeping services for start ups and small businesses. It needs to both attract bookkeepers to become partners and give clients confidence in the professional network. The partners will use products like Tallymint Web, Brightcolumn.com and MintyLedger.com for start ups, as well as help with tasks using the clients existing accounting software.

A home and subpage design is needed. I'll award the work based on the home design. The minor subpage changes can be worked out in the workroom stage.

The pages for the navigation will be: Home, Services, Locations, Partners, FAQ, Contact

```html
<!DOCTYPE html>
<html lang="en">
<head>
<meta charset="utf-8">
<title>Harbor Ledger Associates</title>
<link href="https://fonts.googleapis.com/css2?family=Open+Sans:wght@300;400;600&display=swap" rel="stylesheet">
<style>
:root{
  --brand-blue:#009edf;
  --slate:#5f5f61;
  --white:#ffffff;
  --ink:#555555;
  --body-text:#444444;
  --soft-text:#cfcfcf;
  --footer-bg:#c8c8c8;
  --footer-ink:#4a4a4a;
  --social:#505050;
}
*{box-sizing:border-box;margin:0;padding:0}
html,body{width:1008px;height:1200px;overflow:hidden}
body{position:relative;font-family:"Open Sans",Arial,sans-serif;background:var(--white)}
.band{position:absolute;left:0;width:1008px}
.hero-top{top:0;height:344px;background:var(--brand-blue)}
.hero-bottom{top:344px;height:308px;background:var(--slate)}
.services{top:652px;height:274px;background:var(--white)}
.partners{top:926px;height:182px;background:var(--brand-blue)}
.site-footer{top:1108px;height:92px;background:var(--footer-bg)}

.main-nav{position:absolute;top:24px;left:0;width:1008px;display:flex;justify-content:center;gap:0}
.main-nav a{color:var(--white);text-decoration:none;font-size:12px;text-transform:uppercase;margin:0 21px}

.brand{position:absolute;top:86px;left:422px;display:flex;align-items:center;gap:10px}
.brand-square{width:40px;height:40px;border:3px solid var(--white);border-radius:4px}
.brand-name{color:var(--white);font-size:15px;font-weight:600;line-height:14px;text-transform:uppercase}

.hero-art{position:absolute;left:395px;top:156px;width:212px;height:264px;border-radius:14px;
  background:linear-gradient(160deg,#e6eef4 0%,#b5602f 45%,#7a3a1a 100%)}

.hero-title{position:absolute;top:434px;left:0;width:1008px;text-align:center;color:var(--white);font-weight:300;font-size:40px}
.hero-text{position:absolute;top:504px;left:180px;width:648px;text-align:center;color:var(--soft-text);font-size:12px;line-height:14.5px}
.btn{position:absolute;top:575px;left:436px;width:135px;height:37px;background:var(--brand-blue);color:var(--white);
  font-size:12px;line-height:37px;text-align:center;text-decoration:none;border-radius:2px}

.service{position:absolute;top:702px;width:236px;text-align:center}
.service-icon{width:71px;height:71px;margin:0 auto;background:var(--brand-blue);border-radius:5px;display:flex;align-items:center;justify-content:center}
.service-title{margin-top:11px;font-size:16px;font-weight:400;color:var(--ink)}
.service-text{margin-top:10px;text-align:left;font-size:11px;line-height:13px;color:var(--body-text)}

.tagline{position:absolute;top:951px;left:0;width:1008px;text-align:center;color:var(--white);font-size:15px;line-height:19px}
.partner{position:absolute;top:1032px;display:flex;align-items:center;gap:10px;color:var(--white);font-size:26px;font-weight:300}
.partner-dot{width:48px;height:48px;border-radius:50%;background:var(--white)}

.footer-brand{position:absolute;top:1143px;left:107px;display:flex;align-items:center;gap:8px}
.footer-brand .brand-square{width:26px;height:26px;border:2px solid var(--footer-ink);border-radius:3px}
.footer-brand .brand-name{color:var(--footer-ink);font-size:10px;line-height:9px}
.copyright{position:absolute;top:1153px;left:243px;font-family:Arial,sans-serif;font-size:10px;color:var(--footer-ink)}
.footer-nav{position:absolute;top:1153px;left:382px;display:flex;gap:8px}
.footer-nav a{font-family:Arial,sans-serif;font-size:10px;color:var(--footer-ink);text-decoration:none}
.social{position:absolute;top:1148px;left:776px;display:flex;gap:8px}
.social span{width:23px;height:23px;border-radius:50%;background:var(--social)}
</style>
</head>
<body>
<header class="band hero-top"></header>
<section class="band hero-bottom"></section>
<section class="band services"></section>
<section class="band partners"></section>
<footer class="band site-footer"></footer>

<nav class="main-nav">
  <a href="#">Home</a><a href="#">Services</a><a href="#">Locations</a><a href="#">Partners</a><a href="#">FAQ</a><a href="#">Contact</a>
</nav>

<div class="brand">
  <span class="brand-square"></span>
  <span class="brand-name">Harbor<br>Ledger<br>Associates</span>
</div>

<div class="hero-art" role="img" aria-label="Illustration of a bronze calculator with a pencil and paper documents"></div>

<h1 class="hero-title">Why Choose Our Services</h1>
<p class="hero-text">Beciegast nveriti vitaesaert asety kertya aset aplica binerafae kertyu estyasnemo faserani ptaiades kertyaser daesraeds. Casrolern atur aut oditaut. Binsequuntur magni dolqui ratione volmsequi nesciu orbosas numquam eius modi eincidunt, ut labore et dolore magnam.</p>
<a class="btn" href="#">read more</a>

<div class="service" style="left:108px">
  <div class="service-icon">
    <svg width="26" height="34" viewBox="0 0 26 34" aria-hidden="true"><rect x="1" y="1" width="24" height="32" rx="2" fill="none" stroke="#fff" stroke-width="2"/><rect x="5" y="5" width="16" height="6" fill="#fff"/><g fill="#fff"><rect x="5" y="15" width="4" height="3"/><rect x="11" y="15" width="4" height="3"/><rect x="17" y="15" width="4" height="3"/><rect x="5" y="21" width="4" height="3"/><rect x="11" y="21" width="4" height="3"/><rect x="17" y="21" width="4" height="3"/><rect x="5" y="27" width="4" height="3"/><rect x="11" y="27" width="4" height="3"/><rect x="17" y="27" width="4" height="3"/></g></svg>
  </div>
  <h2 class="service-title">Accounting</h2>
  <p class="service-text">Wolore sereledusempquibderumoms odes necessitatibus saepe evenired­ums estu Etoluptates estudesu usandaeltaque earumul rerum hic tenetura sapientemi delecut mode.</p>
</div>
<div class="service" style="left:385px">
  <div class="service-icon">
    <svg width="38" height="30" viewBox="0 0 38 30" aria-hidden="true"><g fill="none" stroke="#fff" stroke-width="2"><rect x="1" y="2" width="10" height="26"/><rect x="13" y="2" width="10" height="26"/><rect x="26" y="3" width="9" height="25" transform="rotate(-12 30 16)"/></g><g fill="#fff"><rect x="4" y="6" width="4" height="8"/><rect x="16" y="6" width="4" height="8"/><circle cx="6" cy="22" r="1.5"/><circle cx="18" cy="22" r="1.5"/></g></svg>
  </div>
  <h2 class="service-title">Bookkeeping</h2>
  <p class="service-text">Wolore sereledusempquibderumoms odes necessitatibus saepe evenired­ums estu Etoluptates estudesu usandaeltaque earumul rerum hic tenetura sapientemi delecut mode.</p>
</div>
<div class="service" style="left:660px">
  <div class="service-icon">
    <svg width="32" height="32" viewBox="0 0 32 32" aria-hidden="true"><rect x="2" y="5" width="28" height="25" rx="2" fill="none" stroke="#fff" stroke-width="2"/><rect x="2" y="5" width="28" height="6" fill="#fff"/><rect x="8" y="1" width="3" height="7" fill="#fff"/><rect x="21" y="1" width="3" height="7" fill="#fff"/><g fill="none" stroke="#fff" stroke-width="1.2"><path d="M6 15h20M6 20h20M6 25h20M11 13v14M16 13v14M21 13v14"/></g></svg>
  </div>
  <h2 class="service-title">Tax Planning</h2>
  <p class="service-text">Wolore sereledusempquibderumoms odes necessitatibus saepe evenired­ums estu Etoluptates estudesu usandaeltaque earumul rerum hic tenetura sapientemi delecut mode.</p>
</div>

<p class="tagline">Experience and competency in complex numerical manipulations<br>Scrupulous accounting for your business.</p>
<div class="partner" style="left:111px"><span class="partner-dot"></span>Tallymint Web</div>
<div class="partner" style="left:400px">MintyLedger.com</div>
<div class="partner" style="left:712px">Brightcolumn.com</div>

<div class="footer-brand">
  <span class="brand-square"></span>
  <span class="brand-name">Harbor<br>Ledger<br>Associates</span>
</div>
<p class="copyright">© Copyright 2014</p>
<nav class="footer-nav">
  <a href="#">Home</a><a href="#">Services</a><a href="#">Locations</a><a href="#">Partners</a><a href="#">FAQ</a><a href="#">Contact</a><a href="#">Privacy Policy</a><a href="#">Terms</a>
</nav>
<div class="social" aria-label="Social links"><span></span><span></span><span></span><span></span></div>
</body>
</html>
```